Business Card

We need some ideas for corporate business cards. I'm interested in a double sided card, with one side featuring our corporate logo, the other side with employee information.

Corporate colors, logo etc. available at www.brivalo.com

Industry/Entity Type

Business

Requirements
Must have
• The "Brivalo" logo with stylized "O"

Nice to have
• Preferred font is calibri

```html
<!DOCTYPE html>
<html lang="en">
<head>
<meta charset="utf-8">
<title>Brivalo Business Card</title>
<link rel="stylesheet" href="https://fonts.googleapis.com/css2?family=Carlito:wght@400;700&display=swap">
<style>
  :root {
    --brand-blue: #4a6394;
    --text-grey: #8d8d8d;
    --paper: #ffffff;
    --backdrop: #dcdcdc;
    --card-font: "Carlito", "Calibri", sans-serif;
  }
  * { box-sizing: border-box; margin: 0; padding: 0; }
  html, body {
    width: 1200px;
    height: 823px;
    overflow: hidden;
    background: var(--backdrop);
    font-family: var(--card-font);
  }
  .stage {
    position: relative;
    width: 1200px;
    height: 823px;
  }
  .card {
    position: absolute;
    top: 266px;
    width: 510px;
    height: 290px;
    clip-path: polygon(28px 0, calc(100% - 28px) 0, 100% 28px, 100% calc(100% - 28px), calc(100% - 28px) 100%, 28px 100%, 0 calc(100% - 28px), 0 28px);
  }
  .card--back {
    left: 60px;
    background: var(--brand-blue);
    display: flex;
    align-items: center;
    justify-content: center;
    color: var(--paper);
  }
  .web-address {
    display: flex;
    align-items: baseline;
    gap: 4px;
  }
  .web-address__affix {
    font-size: 13px;
    opacity: 0.85;
    letter-spacing: 0.5px;
  }
  .web-address__name {
    font-size: 44px;
    font-weight: 700;
    letter-spacing: 3px;
    text-transform: uppercase;
  }
  .card--front {
    left: 630px;
    background: var(--paper);
    padding: 36px 30px;
    color: var(--text-grey);
    font-size: 14px;
    line-height: 1.1;
  }
  .holder__name {
    color: var(--brand-blue);
    font-weight: 700;
    font-size: 17px;
  }
  .holder__role { font-size: 13px; }
  .address { margin-top: 46px; }
  .contact-row {
    display: flex;
    gap: 12px;
  }
  .contact-row__label {
    width: 10px;
    color: var(--brand-blue);
    font-weight: 700;
    font-size: 13px;
  }
  .phones { margin-top: 12px; }
  .online { margin-top: 12px; }
  .online strong { font-weight: 700; }
  .brand-mark {
    position: absolute;
    right: 34px;
    top: 118px;
    display: flex;
    align-items: center;
    gap: 10px;
    color: var(--brand-blue);
    font-weight: 700;
    font-size: 30px;
  }
  .brand-mark__square {
    width: 22px;
    height: 22px;
    background: var(--brand-blue);
  }
</style>
</head>
<body>
<main class="stage">
  <section class="card card--back" aria-label="Card back">
    <p class="web-address">
      <span class="web-address__affix">www.</span>
      <span class="web-address__name">Brivalo</span>
      <span class="web-address__affix">.com</span>
    </p>
  </section>

  <section class="card card--front" aria-label="Card front">
    <h1 class="holder__name">CARDHOLDER NAME</h1>
    <p class="holder__role">Designation</p>

    <p class="address">01 Avenue, Sunset Boulevard,<br>Your City, Country</p>

    <div class="phones">
      <p class="contact-row"><span class="contact-row__label">T</span><span>+01 0123 4567 8</span></p>
      <p class="contact-row"><span class="contact-row__label">F</span><span>+01 0123 4567 9</span></p>
    </div>

    <div class="online">
      <p class="contact-row"><span class="contact-row__label">E</span><span>cardholder.name@brivalo.com</span></p>
      <p class="contact-row"><span class="contact-row__label">W</span><span><strong>brivalo</strong>.com</span></p>
    </div>

    <div class="brand-mark">
      <span class="brand-mark__square"></span>
      <span class="brand-mark__name">Brivalo</span>
    </div>
  </section>
</main>
</body>
</html>
```